Skyvault Ep Album Art

I'm in a hip-hop/reggae/rock band called Skyvault. We're looking for artwork for our new Ep that we will be releasing in January. The Ep is titled " Drift".

We have a 508/Overtide/Gravel Kid's vibe. We're looking for a cd cover that will capture our vibe. In the past artists have gone with too much of a "reggae" stoner vibe. We don't want Rasta Colors or Jamaican references. We are looking for a more urban vibe. We are way into things that represent LA. For think Downtown LA Skyline, Hollywood, The San Fernando Valley. Basically things that resmble LA. Please feel free to grab our current logo off our facebook page and make it better or incorporate it into other ideas if you see fit.

We don't want anything TOO URBAN, some graffiti fonts/vibes would be great but we aren't a FULL BLOWN rap group. Please listen to our music and try to get our vibe. The Ep is titled "Drift" so something that also projects progress and moving forward as people and as artists is something we also want to project.

Check our music out on our facebook page www.fanwall.example/skyvaultmusic or on YouTube www.clipstream.example/musicskyvault.

An example of a logo band we are way into is band called Morvelle. Feel free to look them up on facebook. We also really like Curtis Palmer's artwork.

Target Market(s)

Skaters, stoners, hip-hop fans, surfers, youth, beach goers etc...

Industry/Entity Type

Artists

Requirements
Nice to have
• Our logo from our facebook page. Could be a cool idea but not necessary. If you come up with a new logo that we could use for album art but also purpose as a new GENERAL logo that would be DOPE!I've attached it, but the font is terrible if someone can change the font that would be great.
Should not have
• Reggae Colors, weed, rasta lions, jamacian influence

```html
<!DOCTYPE html>
<html lang="en">
<head>
<meta charset="utf-8">
<title>Skyvault – Drift EP Cover</title>
<link rel="stylesheet" href="https://fonts.googleapis.com/css2?family=Bungee&family=Saira+Condensed:wght@700&display=swap">
<style>
  :root {
    --frame-grey: #c4c3c6;
    --frame-line: #8e8d91;
    --letter-light: #f1e6ee;
    --hatch-line: #9a6c8c;
    --magenta-deep: #7c1b58;
    --violet: #4a2a62;
    --slate-dark: #2d2934;
    --ink: #1c1a21;
    --band-name: #dddbe0;
  }
  html, body {
    margin: 0;
    padding: 0;
    width: 1200px;
    height: 1200px;
    overflow: hidden;
    background: var(--frame-grey);
  }
  .cover {
    position: relative;
    width: 1200px;
    height: 1200px;
    background:
      repeating-linear-gradient(45deg, var(--frame-line) 0 1.5px, var(--frame-grey) 1.5px 5px);
  }
  .artwork {
    position: absolute;
    left: 50px;
    top: 50px;
    width: 1102px;
    height: 1102px;
    overflow: hidden;
    background:
      radial-gradient(ellipse 30% 26% at 42% 2%, rgba(60, 150, 170, 0.8), transparent 70%),
      radial-gradient(ellipse 22% 20% at 36% 1%, rgba(150, 90, 200, 0.6), transparent 70%),
      radial-gradient(ellipse 55% 70% at 0% 45%, rgba(160, 30, 105, 0.85), transparent 75%),
      radial-gradient(ellipse 60% 45% at 100% 10%, rgba(110, 100, 125, 0.75), transparent 70%),
      linear-gradient(160deg, var(--magenta-deep) 0%, var(--violet) 40%, var(--slate-dark) 72%, var(--ink) 100%);
  }
  .grunge {
    position: absolute;
    inset: 0;
    background:
      repeating-linear-gradient(0deg, rgba(255,255,255,0.025) 0 2px, transparent 2px 7px),
      repeating-linear-gradient(90deg, rgba(0,0,0,0.06) 0 1px, transparent 1px 9px);
  }
  .grunge-patch {
    position: absolute;
    background: rgba(255, 255, 255, 0.05);
  }
  .grunge-patch.dark { background: rgba(0, 0, 0, 0.12); }
  .title-mark {
    position: absolute;
    inset: 0;
  }
  .title-letter {
    font-family: 'Bungee', sans-serif;
    font-size: 410px;
    fill: url(#letter-hatch);
  }
  .band-name {
    font-family: 'Saira Condensed', sans-serif;
    font-weight: 700;
    font-size: 82px;
    letter-spacing: 6px;
    fill: var(--band-name);
  }
</style>
</head>
<body>
  <div class="cover">
    <div class="artwork">
      <div class="grunge"></div>
      <div class="grunge-patch" style="left:620px;top:40px;width:260px;height:180px"></div>
      <div class="grunge-patch dark" style="left:760px;top:260px;width:300px;height:220px"></div>
      <div class="grunge-patch" style="left:880px;top:560px;width:190px;height:260px"></div>
      <div class="grunge-patch dark" style="left:600px;top:700px;width:240px;height:200px"></div>
      <div class="grunge-patch" style="left:460px;top:120px;width:140px;height:340px"></div>
    </div>
    <svg class="title-mark" width="1200" height="1200" viewBox="0 0 1200 1200" role="img" aria-label="Drift by Skyvault">
      <defs>
        <pattern id="letter-hatch" width="5" height="5" patternUnits="userSpaceOnUse" patternTransform="rotate(45)">
          <rect width="5" height="5" fill="var(--letter-light)"/>
          <rect width="1.3" height="5" fill="var(--hatch-line)" opacity="0.55"/>
        </pattern>
      </defs>
      <text class="title-letter" x="106" y="425" textLength="252" lengthAdjust="spacingAndGlyphs">D</text>
      <text class="title-letter" x="395" y="425" textLength="235" lengthAdjust="spacingAndGlyphs">R</text>
      <text class="title-letter" x="106" y="755" textLength="252" lengthAdjust="spacingAndGlyphs">I</text>
      <text class="title-letter" x="395" y="755" textLength="235" lengthAdjust="spacingAndGlyphs">F</text>
      <text class="title-letter" x="106" y="1080" textLength="275" lengthAdjust="spacingAndGlyphs">T</text>
      <text class="band-name" x="698" y="1078" textLength="410" lengthAdjust="spacingAndGlyphs">SKYVAULT</text>
    </svg>
  </div>
</body>
</html>
```